Flyer-Design für psychologische Beratungspraxis für Mütter
Zielgruppe
Gelassenheitswerkstatt ist eine psychologische Beratungspraxis. Ich unterstütze Mütter, Schwangere und Frauen mit Kinderwunsch bei Herausforderungen rund um Schwangerschaft, Geburt, Mutterschaft, und damit einhergehenden Problemen.
Aufgabenstellung
Text nochmal geringgradig geändert...siehe Datei anbei

```html
<!DOCTYPE html>
<html lang="de">
<head>
<meta charset="utf-8">
<title>Gelassenheitswerkstatt – Flyer</title>
<link rel="stylesheet" href="https://fonts.googleapis.com/css2?family=Archivo:wght@800&family=Arimo:wght@400;700&display=swap">
<style>
  :root {
    --backdrop: #e4e3df;
    --paper: #f4f4f2;
    --navy: #27318a;
    --navy-soft: #3f4796;
    --pill: #e9e9ee;
    --fold: rgba(255,255,255,0.35);
  }
  * { margin: 0; padding: 0; box-sizing: border-box; }
  html, body { width: 1200px; height: 864px; overflow: hidden; background: var(--backdrop); }
  body { font-family: "Arimo", Arial, sans-serif; color: var(--navy); }

  .flyer {
    position: absolute; left: 60px; top: 197px;
    width: 1080px; height: 470px;
    display: flex;
    box-shadow: 0 14px 30px rgba(0,0,0,0.18);
  }
  .panel { position: relative; height: 100%; }
  .panel--back { width: 372px; background: var(--paper); }
  .panel--flap { width: 130px; }
  .panel--cover { width: 578px; border-left: 1px solid var(--fold); }

  .photo {
    position: absolute; left: 372px; top: 0; width: 708px; height: 100%;
    background:
      radial-gradient(ellipse 45% 55% at 68% 58%, #e9b9a3 0%, #c98d72 40%, rgba(150,110,95,0) 75%),
      radial-gradient(ellipse 40% 50% at 95% 70%, #7a5446 0%, rgba(122,84,70,0) 80%),
      linear-gradient(110deg, #d3d6dc 0%, #9fa6b1 35%, #8c93a0 60%, #6d6a6e 100%);
  }

  .brand {
    position: absolute; display: flex; align-items: center; gap: 8px;
    font-weight: 700; font-size: 14px; letter-spacing: 0.02em;
  }
  .brand__dot { width: 16px; height: 16px; border-radius: 50%; background: var(--navy); }
  .brand--back { left: 54px; top: 150px; color: var(--navy); }
  .brand--cover { right: 36px; top: 300px; color: #f3ece8; font-size: 12px; }
  .brand--cover .brand__dot { width: 12px; height: 12px; background: #f3ece8; }

  .contact { position: absolute; left: 54px; top: 262px; font-size: 11.5px; line-height: 1.35; color: var(--navy-soft); }
  .contact__title { font-weight: 700; font-size: 13px; color: var(--navy); margin-bottom: 14px; letter-spacing: 0.01em; }
  .contact__name { font-weight: 700; color: var(--navy); }
  .contact__gap { height: 16px; }

  .languages { position: absolute; right: 34px; top: 404px; display: flex; gap: 6px; }
  .languages svg { display: block; width: 22px; height: 14px; }

  .headline { position: absolute; left: 56px; top: 158px; }
  .headline__pill {
    display: inline-block; background: var(--pill); border-radius: 14px;
    font-family: "Archivo", "Arial Black", sans-serif; font-weight: 800;
    font-size: 22px; letter-spacing: 0.04em; color: var(--navy);
    padding: 4px 16px; margin-bottom: 6px;
  }
  .headline__pill--second { margin-left: 28px; }
  .headline__sub { margin: 8px 0 0 44px; font-size: 11.5px; line-height: 1.35; color: var(--navy); }
</style>
</head>
<body>
  <div class="flyer">
    <div class="photo" role="img" aria-label="Foto: Erwachsene Hände halten behutsam einen kleinen Babyfuß vor unscharfem, hellgrauem Hintergrund"></div>

    <section class="panel panel--back">
      <div class="brand brand--back"><span class="brand__dot"></span>Gelassenheitswerkstatt</div>

      <div class="contact">
        <p class="contact__title">KRISENBEGLEITUNG &amp; LEBENSBERATUNG</p>
        <p class="contact__name">Dr. Marlene Vantorin</p>
        <p>Systemische Beraterin (VSBB)</p>
        <p>Heilpraktikerin für Psychotherapie</p>
        <div class="contact__gap"></div>
        <p>www.gelassenheitswerkstatt.de</p>
        <p>info@gelassenheitswerkstatt.de</p>
        <div class="contact__gap"></div>
        <p>0152 000 41 758</p>
      </div>

      <div class="languages" aria-label="Beratungssprachen: Deutsch, Italienisch, Englisch, Französisch">
        <svg viewBox="0 0 3 2"><rect width="3" height="2" fill="#000"/><rect y=".667" width="3" height=".667" fill="#dd0000"/><rect y="1.333" width="3" height=".667" fill="#ffce00"/></svg>
        <svg viewBox="0 0 3 2"><rect width="1" height="2" fill="#009246"/><rect x="1" width="1" height="2" fill="#fff"/><rect x="2" width="1" height="2" fill="#ce2b37"/></svg>
        <svg viewBox="0 0 30 20"><rect width="30" height="20" fill="#012169"/><path d="M0 0L30 20M30 0L0 20" stroke="#fff" stroke-width="4"/><path d="M0 0L30 20M30 0L0 20" stroke="#c8102e" stroke-width="1.5"/><path d="M15 0V20M0 10H30" stroke="#fff" stroke-width="6"/><path d="M15 0V20M0 10H30" stroke="#c8102e" stroke-width="3.5"/></svg>
        <svg viewBox="0 0 3 2"><rect width="1" height="2" fill="#0055a4"/><rect x="1" width="1" height="2" fill="#fff"/><rect x="2" width="1" height="2" fill="#ef4135"/></svg>
      </div>
    </section>

    <section class="panel panel--flap"></section>

    <section class="panel panel--cover">
      <div class="headline">
        <span class="headline__pill">KRISENBEGLEITUNG</span><br>
        <span class="headline__pill headline__pill--second">UND LEBENSBERATUNG</span>
        <p class="headline__sub">Psychologische Beratungspraxis für Mütter,<br>Schwangere und Frauen mit Kinderwunsch</p>
      </div>
      <div class="brand brand--cover"><span class="brand__dot"></span>Gelassenheitswerkstatt</div>
    </section>
  </div>
</body>
</html>
```